High end Electrical/home automation Business Card

Need a card for a high end electrical and home automation company utilising the existing logo.
Phone
Email
Website

Like black look with raised detail. Don’t necessarily need to keep colour of logo it could be made grayscale or white etc

Target Market(s)

High end clients

Contact Information for Business Card

Ridgeline Electrical

Requirements
Must have
• Logo, phone, email, website, address

High end look
Nice to have
• Black background card
Raised font
Should not have
• Lots of colour

```html
<!DOCTYPE html>
<html lang="en">
<head>
<meta charset="utf-8">
<title>Ridgeline Electrical – Business Card</title>
<link rel="stylesheet" href="https://fonts.googleapis.com/css2?family=Roboto:wght@400;500&family=Roboto+Condensed:wght@400;700&display=swap">
<style>
  :root {
    --page: #ffffff;
    --bleed: #a7a7a7;
    --card-black: #000000;
    --card-white: #ffffff;
    --logo-grey: #3b3b3b;
    --text-light: #d9d9d9;
    --text-grey: #808080;
    --divider: #4a4a4a;
  }
  * { margin: 0; padding: 0; box-sizing: border-box; }
  html, body { width: 1200px; height: 1200px; overflow: hidden; background: var(--page); }
  body { position: relative; font-family: "Roboto", Arial, sans-serif; }

  .bleed-area { position: absolute; background: var(--bleed); }
  .bleed-label {
    position: absolute; font-size: 12px; color: #000;
    font-family: "Roboto", Arial, sans-serif; line-height: 1;
  }
  .bleed-label--side { transform: rotate(90deg); transform-origin: left top; }

  .card {
    position: absolute; width: 521px; height: 298px;
    border-radius: 42px; overflow: hidden; background: var(--card-black);
  }

  /* Front */
  .front { left: 168px; top: 174px; }
  .front-mark {
    position: absolute; left: 50%; top: 70px; width: 92px; height: 92px;
    margin-left: -46px; border-radius: 50%; background: var(--logo-grey);
  }
  .front-name {
    position: absolute; left: 0; right: 0; top: 176px; text-align: center;
    font-family: "Roboto Condensed", Arial, sans-serif; font-weight: 700;
    font-size: 29px; color: var(--logo-grey); letter-spacing: -0.3px;
  }
  .front-web {
    position: absolute; left: 0; right: 0; top: 212px; text-align: center;
    font-size: 13px; letter-spacing: 2px; color: var(--logo-grey); font-weight: 500;
  }

  /* Back */
  .back { left: 567px; top: 780px; }
  .back-header {
    position: absolute; left: 0; top: 0; width: 100%; height: 106px;
    background: var(--card-white); text-align: center;
  }
  .person-name {
    padding-top: 33px; font-family: "Roboto Condensed", Arial, sans-serif;
    font-weight: 700; font-size: 23px; color: #000; letter-spacing: 0.5px;
  }
  .person-title {
    margin-top: 2px; font-size: 13px; letter-spacing: 3.4px; color: var(--text-grey);
  }
  .contact-list { position: absolute; left: 34px; top: 142px; list-style: none; }
  .contact-item { display: flex; align-items: center; margin-bottom: 13px; height: 30px; }
  .contact-icon { width: 26px; height: 26px; margin-right: 22px; flex: none; }
  .contact-text { font-size: 14px; line-height: 1.3; color: var(--text-light); }
  .contact-text--small { font-size: 13px; }
  .divider {
    position: absolute; left: 350px; top: 135px; width: 2px; height: 130px;
    background: var(--divider);
  }
  .social { position: absolute; left: 395px; top: 182px; display: flex; gap: 10px; }
  .social-dot { width: 22px; height: 22px; border-radius: 50%; background: var(--text-light); }
</style>
</head>
<body>

  <!-- Front side -->
  <div class="bleed-area" style="left:149px; top:155px; width:559px; height:335px;"></div>
  <span class="bleed-label bleed-label--side" style="left:167px; top:291px;">bleed</span>
  <span class="bleed-label" style="left:346px; top:476px;">bleed</span>
  <section class="card front" aria-label="Card front">
    <div class="front-mark"></div>
    <p class="front-name">Ridgeline Electrical</p>
    <p class="front-web">www.ridgelineelectrical.com</p>
  </section>

  <!-- Back side -->
  <div class="bleed-area" style="left:548px; top:761px; width:559px; height:335px;"></div>
  <span class="bleed-label bleed-label--side" style="left:566px; top:946px;">bleed</span>
  <span class="bleed-label" style="left:745px; top:1082px;">bleed</span>
  <section class="card back" aria-label="Card back">
    <header class="back-header">
      <h1 class="person-name">DANIEL MERCER</h1>
      <p class="person-title">CORPORATE MANAGER</p>
    </header>

    <ul class="contact-list">
      <li class="contact-item">
        <svg class="contact-icon" viewBox="0 0 26 26" aria-hidden="true">
          <circle cx="13" cy="13" r="13" fill="#fff"/>
          <path d="M7 10c0-2 2-3 6-3s6 1 6 3v1.5h-3V10h-6v1.5H7z M8.5 13h9l1 5.5h-11z" fill="#000"/>
        </svg>
        <span class="contact-text">1.555.012.3456</span>
      </li>
      <li class="contact-item">
        <svg class="contact-icon" viewBox="0 0 26 26" aria-hidden="true">
          <circle cx="13" cy="13" r="13" fill="#fff"/>
          <path d="M13 6l7.5 6.5h-2V19h-3.5v-4h-4v4H7.5v-6.5h-2z" fill="#000"/>
        </svg>
        <span class="contact-text contact-text--small">482 Alder Grove Lane<br>Concord, NH 03301</span>
      </li>
      <li class="contact-item">
        <svg class="contact-icon" viewBox="0 0 26 26" aria-hidden="true">
          <circle cx="13" cy="13" r="13" fill="#fff"/>
          <rect x="6.5" y="8.5" width="13" height="9.5" rx="1" fill="#000"/>
          <path d="M7 9.5l6 4.5 6-4.5" stroke="#fff" stroke-width="1.3" fill="none"/>
        </svg>
        <span class="contact-text contact-text--small">danielmercer@ridgelineelectrical.com</span>
      </li>
    </ul>

    <div class="divider"></div>

    <div class="social" aria-label="Social media">
      <span class="social-dot"></span>
      <span class="social-dot"></span>
      <span class="social-dot"></span>
    </div>
  </section>

</body>
</html>
```